依頼詳細
マッサージ店のデザイン看板をお願いします。

国家資格のマッサージ師が施術してくれる安心感を見る人に与えてくれたらありがたいです。
お洒落で目立つ看板をぜひお願いします。
記載項目
国家資格者で安心 ひだまり堂マッサージ

料金
40分…4,000円(税込)
60分…6,000円(税込)
80分…8,000円(税込)
100分…10,000円(税込)

☏043-582-7190
希望イメージ
シンプル 複雑
単色 カラフル
暗い 明るい
日常 高級
遊び心 厳粛
未来的 伝統的
女性的 男性的
希望する色
黄・オレンジ系、青系
納品ファイル
• イラストレーター形式 (.ai)
補足説明
原稿サイズ W470mm×H990mm
表示画面 W420mm×H940mm

・料金表の表示は小さめで大丈夫です。
・国家資格者で安心 ひだまり堂マッサージ の文字を目立つようにぜひお願いします。
依頼内容に二つの画像を表示するようにお願いしていたのですが・・・。
どうか二つの画像を看板デザインに必ず入れてください。よろしくお願いします。

・施術中の画像を大きく表示をお願いします。
・私のイラスト画像は小さめの表示をお願いします。
当初添付した施術中の画像は、小さかったようですみませんでした。
大きめの画像を皆様からご希望頂きましたので施術用の画像はこちらの画像でよろしくお願いします。
当初、マッサージ施術の画像は必ず当店の施術中の画像を必ず使ってください。
と掲載いたしました。

しかし皆様からデザインして頂いている他のマッサージ画像でも結構いい画像があるということを感じました。
ですのでもし他のマッサージ画像でのデザインも見たいのでもしいいマッサージ画像がありましたらぜひぜひよろしくお願いいたします。
皆さまいろいろなデザインを提案していただきありがとうございます。すごく嬉しいです。

明るめでややカラフルのデザインを希望イメージで掲載しておりますがお洒落系なデザインも見てみたいのでぜひお洒落系なデザインもよろしくお願いします。

記載項目に
予約優先
ひだまり堂マッサージ 検索 ☝
当店のQRコード https://www.yurunoteya.jp/
以上3点の追加をよろしくお願いします。
皆さま沢山のデザインをご提案いただきありがとうございます。

①国家資格者で安心 ひだまり堂マッサージ の書体を丸ゴシック
②国家資格者で安心 ひだまり堂マッサージ の書体をポップ体
以上2点のデザインを見てみたいのでよろしくお願いします。

看板はすでに買いました。
なおこちらの看板店の「データ入稿のご注意事項」https://item.kaimonomori.jp/sorahyoshiki/c/0000000382/を一応ご確認ください。

沢山のご提案をしていただきました。そしてどのデザインも自分が描いていたイメージに近い物が多かったです。修正提案にも丁寧に応じていただき助かりました!!

今回初めてこちらのシステムを利用させていただきました。
皆さまから沢山のご提案をいただきすごく迷ってしまうほどでした。
またの機会もよろしくお願いします。

```html
<!DOCTYPE html>
<html lang="ja">
<head>
<meta charset="utf-8">
<title>ひだまり堂マッサージ 看板</title>
<link rel="stylesheet" href="https://fonts.googleapis.com/css2?family=M+PLUS+1p:wght@700;800;900&display=swap">
<style>
  :root {
    --red: #e3321e;
    --orange: #f07a1a;
    --blue: #1d6fc4;
    --blue-dark: #14508f;
    --ink: #1d3a6b;
    --white: #ffffff;
    --frame: #d9dde3;
    --photo-a: #f3ede6;
    --photo-b: #7c9fd1;
    --xray-a: #0d1d4a;
    --xray-b: #3a5fb0;
    --pain: #f59a2a;
  }
  * { box-sizing: border-box; margin: 0; padding: 0; }
  html, body { width: 1200px; height: 2532px; overflow: hidden; background: var(--white); }
  body { font-family: "M PLUS 1p", sans-serif; position: relative; }
  .signboard { position: absolute; inset: 0; border: 8px solid var(--frame); background: var(--white); }

  .headline { position: absolute; left: 70px; top: 70px; width: 1060px; height: 520px; }
  .headline__lead { position: absolute; left: 20px; top: 40px; font-size: 112px; font-weight: 900; color: var(--ink); letter-spacing: 2px; line-height: 1; }
  .headline__badge { position: absolute; right: 20px; top: 10px; width: 200px; height: 270px; background: var(--orange); border: 8px solid var(--red); border-radius: 14px; color: var(--white); font-size: 122px; font-weight: 900; line-height: 122px; text-align: center; padding-top: 6px; }
  .headline__name { position: absolute; left: 10px; top: 200px; font-size: 156px; font-weight: 900; color: var(--red); line-height: 1.06; letter-spacing: 2px; }

  .specialty { position: absolute; left: 30px; top: 590px; width: 1140px; height: 140px; background: var(--blue); border: 6px solid var(--blue-dark); color: var(--white); font-size: 100px; font-weight: 900; text-align: center; line-height: 126px; letter-spacing: 2px; }

  .treatment-photo { position: absolute; left: 30px; top: 745px; width: 1140px; height: 680px; background: linear-gradient(160deg, var(--photo-a) 0%, #e9d7c6 45%, var(--photo-b) 100%); }
  .owner-portrait { position: absolute; left: 940px; top: 1190px; width: 210px; height: 210px; border-radius: 50%; background: linear-gradient(180deg, #f6e0c8, #3a4f7a); border: 4px solid var(--white); }

  .symptom__label { position: absolute; height: 100px; background: var(--orange); border-radius: 50px; color: var(--white); font-size: 72px; font-weight: 900; text-align: center; line-height: 100px; }
  .symptom__image { position: absolute; background: radial-gradient(circle at 55% 40%, var(--pain) 0%, #c2461c 14%, var(--xray-b) 40%, var(--xray-a) 100%); }

  .price { position: absolute; left: 640px; top: 1900px; width: 520px; }
  .price__title { font-size: 56px; font-weight: 800; color: var(--ink); padding-left: 40px; line-height: 80px; }
  .price__row { display: flex; height: 80px; margin-bottom: 6px; }
  .price__time { width: 170px; border: 4px solid var(--blue); background: var(--white); color: var(--ink); font-size: 54px; font-weight: 800; text-align: center; line-height: 72px; }
  .price__fee { flex: 1; background: var(--blue); color: var(--white); font-size: 58px; font-weight: 800; text-align: right; padding-right: 24px; line-height: 80px; }
  .price__fee small { font-size: 34px; }

  .contact { position: absolute; left: 30px; top: 2320px; width: 1140px; height: 160px; background: var(--blue); display: flex; align-items: center; justify-content: center; gap: 36px; color: var(--white); font-size: 108px; font-weight: 700; letter-spacing: 2px; }
  .contact__icon { width: 120px; height: 120px; }
</style>
</head>
<body>
<main class="signboard">
  <header class="headline">
    <p class="headline__lead">国家資格者で</p>
    <p class="headline__badge">安<br>心</p>
    <h1 class="headline__name">ひだまり堂<br>マッサージ</h1>
  </header>

  <p class="specialty">指圧・マッサージ専門店</p>

  <div class="treatment-photo" role="img" aria-label="施術者が横になった女性の背中をマッサージしている写真"></div>
  <div class="owner-portrait" role="img" aria-label="店主のイラスト"></div>

  <section class="symptoms">
    <p class="symptom__label" style="left:90px; top:1460px; width:390px;">肩こり</p>
    <div class="symptom__image" role="img" aria-label="肩の痛みを示す人体のイラスト" style="left:70px; top:1580px; width:480px; height:270px;"></div>

    <p class="symptom__label" style="left:720px; top:1460px; width:360px;">首こり</p>
    <div class="symptom__image" role="img" aria-label="首の骨の痛みを示すイラスト" style="left:620px; top:1580px; width:510px; height:270px;"></div>

    <p class="symptom__label" style="left:90px; top:1890px; width:390px;">腰痛</p>
    <div class="symptom__image" role="img" aria-label="腰の痛みを示す人体のイラスト" style="left:70px; top:2010px; width:480px; height:280px;"></div>
  </section>

  <section class="price">
    <h2 class="price__title">料金（税込）</h2>
    <div class="price__row"><span class="price__time">40分</span><span class="price__fee">4,000<small>円</small></span></div>
    <div class="price__row"><span class="price__time">60分</span><span class="price__fee">6,000<small>円</small></span></div>
    <div class="price__row"><span class="price__time">80分</span><span class="price__fee">8,000<small>円</small></span></div>
    <div class="price__row"><span class="price__time">100分</span><span class="price__fee">10,000<small>円</small></span></div>
  </section>

  <footer class="contact">
    <svg class="contact__icon" viewBox="0 0 120 120" aria-hidden="true">
      <circle cx="60" cy="60" r="54" fill="none" stroke="#fff" stroke-width="7"/>
      <path d="M28 52 Q60 28 92 52 L86 62 L74 56 L72 48 Q60 44 48 48 L46 56 L34 62 Z" fill="#fff"/>
      <rect x="40" y="62" width="40" height="28" rx="4" fill="#fff"/>
    </svg>
    <span class="contact__tel">043-582-7190</span>
  </footer>
</main>
</body>
</html>
```